Wattle Ridge Aged Care Centre

We need a website design for an aged care facility in Brisbane (a different one to project already posted) with final design provided as a .psd file.

This website will be built on Dot Net Nuke so design needs to be able to be converted into a DNN skin and containers.

Target Market(s)

• Credibility
• Family orientated
• Establish an online identity
• Download a booking form for tours
• Receive general enquiries
• Feature a phone number
• Advertise career opportunities

Number of Pages Required

1 page

Requirements
Must have
• o The following elements are to be included in the design concepts:
• o Phone number will be featured in banner 07 3914 2786
• o Logo and words Marigold Care Centre to be featured in banner
• o Area for a flash banner of rotating images on homepage (have attached some images)
• o 3 x buttons to be designed and feature on homepage - Book a Tour, Contact Us and Sign up to our newsletter
• o No colour preference but perhaps keeping with their logo/branding but am open to ideas

```html
<!DOCTYPE html>
<html lang="en">
<head>
<meta charset="utf-8">
<title>Marigold Care Centre</title>
<link rel="stylesheet" href="https://fonts.googleapis.com/css2?family=Crimson+Text:wght@400;600&family=Noto+Sans:wght@400;700&display=swap">
<style>
:root{
  --accent:#b5460f;
  --nav-red:#8b1a1a;
  --link-red:#a0321a;
  --ink:#222;
  --cream:#f3f1ea;
  --panel-mission:#ece3c8;
  --beige:#e6d9c4;
  --tan:#d9c6a8;
  --dark-brown:#3a2a20;
  --grey-panel:#c4c2bd;
}
*{margin:0;padding:0;box-sizing:border-box}
html,body{width:1177px;height:1200px;overflow:hidden;background:#fff}
body{position:relative;font-family:"Noto Sans",sans-serif;color:var(--ink)}
.abs{position:absolute}

.banner-photo{left:0;top:0;width:1177px;height:415px;
  background:linear-gradient(180deg,#b9b2a6 0%,#8c6a4c 35%,#5d4a36 60%,#c9a88f 78%,#8f8d88 100%)}
.brand-box{left:922px;top:0;width:204px;height:197px;background:#f5f3ea;
  display:flex;flex-direction:column;align-items:center;justify-content:center;gap:14px}
.brand-box .dot{width:22px;height:22px;border-radius:50%;background:#2d5a2a}
.brand-name{font-family:"Crimson Text",serif;font-weight:600;font-size:22px;color:#2d5a2a;text-align:center;line-height:1.15}
.brand-phone{font-family:"Crimson Text",serif;font-weight:400;font-size:25px;color:#2d5a2a}

.divider{left:0;width:1177px;height:23px;background:linear-gradient(180deg,#efe4d2,#d8c6a9 50%,#efe4d2)}
.divider.top{top:415px}
.divider.bottom{top:1079px;height:21px}

.right-strip{left:1134px;top:438px;width:43px;height:641px;background:linear-gradient(90deg,#d7c7ad,#ece2d2)}

.main-nav{left:0;top:438px;width:1134px;height:77px;display:flex}
.main-nav a{position:relative;flex:1;display:flex;align-items:center;justify-content:center;
  font-family:"Crimson Text",serif;font-size:20px;color:var(--nav-red);text-decoration:none;
  background:linear-gradient(180deg,#fdfdfb,#e4e3dd);border-right:2px solid #cfcac0;letter-spacing:.3px}
.main-nav a::after{content:"";position:absolute;right:0;bottom:0;border-style:solid;border-width:0 0 14px 14px;
  border-color:transparent transparent #9a968e transparent}

.who{left:0;top:515px;width:380px;height:338px;background:var(--cream)}
.mission{left:380px;top:515px;width:754px;height:338px;background:linear-gradient(180deg,#dcd3bd,var(--panel-mission) 30%,#efe6cd)}
.section-title{font-family:"Crimson Text",serif;font-size:28px;color:#222;font-weight:400}
.section-title b{font-weight:400;font-size:36px;color:var(--accent);letter-spacing:-1px}
.who .section-title{position:absolute;left:43px;top:25px}
.who .lead{position:absolute;left:43px;top:92px;font-size:16px;font-weight:700;color:var(--link-red)}
.who .copy{position:absolute;left:43px;top:120px;width:310px;font-size:15.5px;line-height:21px}
.who .copy p+p{margin-top:21px}
.who .more{position:absolute;left:43px;top:282px;font-size:16px;font-weight:700;color:#a0501a;text-decoration:underline}
.mission .section-title{position:absolute;left:47px;top:25px}
.mission .copy{position:absolute;left:55px;top:80px;width:672px;font-size:15.2px;line-height:21px}

.newsletter{left:0;top:853px;width:380px;height:226px;background:linear-gradient(90deg,#e9e8e4,var(--grey-panel))}
.newsletter .art{position:absolute;left:23px;top:35px;width:138px;height:180px;border-radius:14px;
  background:linear-gradient(160deg,#ffffff,#dfe6ee 60%,#f2a23a)}
.newsletter h2{position:absolute;left:184px;top:30px;font-family:"Crimson Text",serif;font-weight:400;
  font-size:30px;line-height:35px;color:var(--link-red);letter-spacing:-.5px}
.newsletter .btn{position:absolute;left:197px;top:173px;width:140px;height:34px;display:flex;align-items:center;justify-content:center;
  background:linear-gradient(180deg,#ffffff,#dddcd7);border:1px solid #aaa;font-size:16px;font-weight:700;color:var(--link-red);text-decoration:none}

.tour{left:380px;top:853px;width:754px;height:226px;background:var(--cream)}
.tour .section-title{position:absolute;left:47px;top:22px}
.tour .photo{position:absolute;left:32px;top:101px;width:144px;height:88px;border:1px solid #777;
  background:linear-gradient(180deg,#6e5440,#a58463 45%,#e6ddd0 70%,#5c4636)}
.tour .lead{position:absolute;left:199px;top:102px;font-size:16px;font-weight:700;color:#111}
.tour ul{position:absolute;left:199px;top:139px;list-style:none;font-size:15px;line-height:22px}
.tour li{display:flex;align-items:center;gap:8px}
.tour li a{color:var(--link-red);text-decoration:underline}

.footer{left:0;top:1100px;width:1134px;height:100px;background:linear-gradient(180deg,#f4ece0,#fbf7f0)}
.footer-strip{left:1134px;top:1100px;width:43px;height:100px;background:var(--dark-brown)}
.footer .emblem{position:absolute;left:69px;top:22px;width:62px;height:52px;border-radius:40%;background:#ddd6cb}
.footer nav{position:absolute;left:230px;top:24px;display:flex;gap:14px;font-size:15px;color:#111}
.footer nav span.sep{color:#777}
.footer nav a{color:#111;text-decoration:none}
.footer .legal{position:absolute;left:420px;top:50px;font-size:15px;color:#111}
.footer .legal a{color:#a0501a;text-decoration:underline}
</style>
</head>
<body>

<header>
  <div class="abs banner-photo" role="img" aria-label="Rotating banner photo of the care centre entrance with columns, timber doors and garden"></div>
  <div class="abs brand-box">
    <span class="dot"></span>
    <div class="brand-name">Marigold<br>Care Centre</div>
    <div class="brand-phone">07 3914 2786</div>
  </div>
</header>

<div class="abs divider top"></div>
<div class="abs right-strip"></div>

<nav class="abs main-nav">
  <a href="#">HOME</a>
  <a href="#">ABOUT US</a>
  <a href="#">FACILITIES</a>
  <a href="#">TOURS</a>
  <a href="#">CAREERS</a>
  <a href="#">CONTACT US</a>
</nav>

<section class="abs who">
  <h2 class="section-title"><b>WHO</b> we are?</h2>
  <div class="lead">Lorem ipsum dolor sit amet</div>
  <div class="copy">
    <p>Sed do eiusmod tempor incididunt amet labore et dolore magna aliqua.</p>
    <p>Ut enim minim veniam, quis noistrud exercitation. ullamco laboris nisi ut aliquip ex ea commodo consequat.</p>
  </div>
  <a class="more" href="#">read more about us</a>
</section>

<section class="abs mission">
  <h2 class="section-title"><b>OUR</b> mission</h2>
  <div class="copy">Tat veros ad molor sequiscipit am ex el digna commodo lorperat landrerate do erillamet prat nonsequat. Ip exero con henim dolorem irit accum nos doloreet, sequat, voloboreet, sum iriusto odiam zzrit luptatis ea faccum quismod tatum iuscil ullum volorem dit nibh etum velesecte feugue faccum venit iustis doloborem nonse faccum quat eugiam, con utat praesed magna corpera esequis eugiat nulluptatet, sis nit, cor ilit delismod dui er iure consed magnibh etuer ipsumsa ndiam, volore duiscinim vercipsum autpat pratum nullamet, quam, vel ulla feum volorper sum nulla ad er senis nummy num voluptat ute veleniam iusci estrud endit prat, sectem alis acilit ulpute velesectet dolum vulla facil ex eugait lore elissisi.<br>Osto commy niat, con et ip ex etum eum nibh et nosto dolor si ex eu faci tat erostrud magna faccummy nibh ea feu facipis accummodo ero od dol</div>
</section>

<section class="abs newsletter">
  <div class="art" role="img" aria-label="Illustration of a newsletter document with an add symbol"></div>
  <h2>SIGN UP<br>TO OUR<br>NEWSLETTER</h2>
  <a class="btn" href="#">more info</a>
</section>

<section class="abs tour">
  <h2 class="section-title"><b>BOOK A</b> tour</h2>
  <div class="photo" role="img" aria-label="Photo of a bright kitchen and dining area"></div>
  <div class="lead">Lorem ipsum dolor sit amet consectetur adipi sitsicingt</div>
  <ul>
    <li><svg width="9" height="9" viewBox="0 0 9 9"><path d="M1 1l4 3.5L1 8M4 1l4 3.5L4 8" fill="none" stroke="#a0321a" stroke-width="1.2"/></svg><a href="#">Sed do eiusmod tempor incididunt ut labore et dolore magna aliqua.</a></li>
    <li><svg width="9" height="9" viewBox="0 0 9 9"><path d="M1 1l4 3.5L1 8M4 1l4 3.5L4 8" fill="none" stroke="#a0321a" stroke-width="1.2"/></svg><a href="#">Ut enim minim veniam, quis noistrud exercitation ullamco laboris.</a></li>
  </ul>
</section>

<div class="abs divider bottom"></div>

<footer class="abs footer">
  <div class="emblem" role="img" aria-label="Faint decorative dove emblem"></div>
  <nav>
    <a href="#">Home</a><span class="sep">:</span>
    <a href="#">About Us</a><span class="sep">:</span>
    <a href="#">Facilities</a><span class="sep">:</span>
    <a href="#">Tours</a><span class="sep">:</span>
    <a href="#">Careers</a><span class="sep">:</span>
    <a href="#">Contacts</a>
  </nav>
  <div class="legal">2009 | &nbsp;<a href="#">Privacy policy</a></div>
</footer>
<div class="abs footer-strip"></div>

</body>
</html>
```